Business Card Design for an Investment Company

We need a business card design for our private investment company, called Ashbourne Partners. Ashbourne Partners is an investments partnership that aims to acquire shares in listed companies with a view to influencing those companies through active dialogue in order to improve their value. We need designs that use the logo colors (blue, grey, white), we need both English and Arabic on the business cards (can be on one side or 2 sides). The final logo should communicate professionalism, conservatism (nothing too fancy or too cheesy), that we are smart, conservative and old school.

Target Market(s)

Investment companies

Industry/Entity Type

Investment

Contact Information for Business Card

Khalid Yousef Rumaithi
Senior Executive Officer

Palm Terrace 07, Level 3, Office 215/12
HLMZ

+9714987650
krumaithi@ashbournepartners.com
www.ashbournepartners.com

Requirements
Must have
• Logo to be placed on the left hand side of the business card
• for the Arabic, we only need to have the name and title so it can be accomodated on one side so we can have the other side with full color and logo. The arabic that needs to be used is the below:
• خالد يوسف الرميثي
• المدير التنفيدي

```html
<!DOCTYPE html>
<html lang="en">
<head>
<meta charset="utf-8">
<title>Ashbourne Partners – Business Card</title>
<link href="https://fonts.googleapis.com/css2?family=Lato:wght@400;700;900&family=Noto+Naskh+Arabic:wght@400&display=swap" rel="stylesheet">
<style>
  :root {
    --bg: #9a9a9a;
    --white: #ffffff;
    --brand-blue: #1a6ea8;
    --band-blue: #1790c4;
    --deep-blue: #0f6aa0;
    --light-blue: #1ea3d0;
    --grey-text: #4d4d4d;
    --rule-grey: #7a7a7a;
  }
  * { margin: 0; padding: 0; box-sizing: border-box; }
  html, body { width: 1200px; height: 900px; overflow: hidden; }
  body {
    background: var(--bg);
    font-family: "Lato", Arial, sans-serif;
    position: relative;
  }
  .card {
    position: absolute;
    width: 600px;
    height: 343px;
    overflow: hidden;
    box-shadow: 0 6px 18px rgba(0,0,0,0.25);
  }
  /* Front */
  .card-front { left: 60px; top: 90px; background: var(--white); }
  .wordmark-front {
    position: absolute; left: 40px; top: 42px;
    display: flex; align-items: center; gap: 12px;
    font-weight: 900; font-size: 34px; color: var(--brand-blue);
    letter-spacing: -0.5px;
  }
  .wordmark-front .mark-square { width: 22px; height: 22px; background: var(--brand-blue); }
  .holder {
    position: absolute; right: 40px; top: 118px; text-align: right;
  }
  .holder-name { font-weight: 700; font-size: 21px; color: var(--grey-text); }
  .holder-title { font-weight: 700; font-size: 14px; color: var(--brand-blue); margin-top: 3px; }
  .holder-arabic {
    font-family: "Noto Naskh Arabic", serif;
    direction: rtl; font-size: 13px; color: var(--band-blue); line-height: 1.5; margin-top: 4px;
  }
  .contact-list {
    position: absolute; left: 40px; top: 208px; list-style: none;
  }
  .contact-list li {
    display: flex; align-items: center; gap: 12px;
    font-size: 14px; color: var(--grey-text); line-height: 22px;
  }
  .contact-list svg { width: 13px; height: 13px; fill: var(--brand-blue); flex: none; }
  .band-rule {
    position: absolute; left: 0; right: 0; bottom: 50px; height: 2px; background: var(--rule-grey);
  }
  .address-band {
    position: absolute; left: 0; right: 0; bottom: 0; height: 46px;
    background: var(--band-blue); color: var(--white);
    font-size: 14px; display: flex; align-items: center; justify-content: flex-end;
    padding-right: 40px;
  }
  /* Back */
  .card-back {
    left: 540px; top: 470px;
    background: radial-gradient(ellipse at 30% 35%, var(--light-blue) 0%, #2a7fb0 45%, var(--deep-blue) 100%);
    display: flex; align-items: center; justify-content: center;
  }
  .wordmark-back {
    display: flex; align-items: center; gap: 14px;
    font-weight: 900; font-size: 40px; color: var(--white); letter-spacing: -0.5px;
  }
  .wordmark-back .mark-square { width: 26px; height: 26px; background: var(--white); }
</style>
</head>
<body>
  <section class="card card-front" aria-label="Business card front">
    <div class="wordmark-front"><span class="mark-square"></span>Ashbourne Partners</div>

    <div class="holder">
      <p class="holder-name">Khalid Yousef Rumaithi</p>
      <p class="holder-title">Senior Executive Officer</p>
      <p class="holder-arabic" lang="ar">خالد يوسف الرميثي<br>المدير التنفيدي</p>
    </div>

    <ul class="contact-list">
      <li>
        <svg viewBox="0 0 24 24" aria-hidden="true"><path d="M6.6 10.8a15 15 0 0 0 6.6 6.6l2.2-2.2c.3-.3.7-.4 1-.2 1.1.4 2.3.6 3.6.6.6 0 1 .4 1 1V20c0 .6-.4 1-1 1A17 17 0 0 1 3 4c0-.6.4-1 1-1h3.5c.6 0 1 .4 1 1 0 1.3.2 2.5.6 3.6.1.3 0 .7-.2 1z"/></svg>
        +9714987650
      </li>
      <li>
        <svg viewBox="0 0 24 24" aria-hidden="true"><path d="M2 5h20v14H2z M2 5l10 8 10-8" fill="none" stroke="#1a6ea8" stroke-width="2"/></svg>
        krumaithi@ashbournepartners.com
      </li>
      <li>
        <svg viewBox="0 0 24 24" aria-hidden="true"><circle cx="12" cy="12" r="10" fill="none" stroke="#1a6ea8" stroke-width="2"/><path d="M2 12h20M12 2c3 3 3 17 0 20M12 2c-3 3-3 17 0 20" fill="none" stroke="#1a6ea8" stroke-width="1.6"/></svg>
        www.ashbournepartners.com
      </li>
    </ul>

    <div class="band-rule"></div>
    <div class="address-band">Palm Terrace 07, Level 3, Office 215/12, HLMZ</div>
  </section>

  <section class="card card-back" aria-label="Business card back">
    <div class="wordmark-back"><span class="mark-square"></span>Ashbourne Partners</div>
  </section>
</body>
</html>
```